GRAPHIC DESIGN FOR RESTAURANT MENU FOR HEALTHY RESTAURANT

I am looking for a graphic design for our menu displayed on a TV screen. Please ensure the file will fit on a TV screen nicely. We are looking for a clean design , with the following items. We would also like to include a couple of photos.
Breakfast:
Protein Chocolate Chip Pancakes - $12.95
Sunny Trail Burrito- $11.95
Tall Barn Omelette - $12.95
Lunch
Butter Chicken - $13.95
Chicken Quesadilla - $13.45
Coconut Garlic Shrimp - $15.95
Goat Cheese Stuffed Chicken - $14.95
Chipotle Steak Wrap - $12.95
Turkey Meatball Fettuccini - $13.45
Chicken Alfredo - $13.45
Chicken Parmesan - $13.95
Pesto Chicken Pasta - $13.45
Steak Bite and Green Stir Fry - $13.45
Asian Chicken Teriyaki - $13.45
Please include our logo
Restaurant

```html
<!DOCTYPE html>
<html lang="en">
<head>
<meta charset="utf-8">
<title>Greenleaf Menu Board</title>
<link rel="stylesheet" href="https://fonts.googleapis.com/css2?family=Oswald:wght@700&family=Questrial&display=swap">
<style>
  :root {
    --page: #ffffff;
    --board: #1c1c1c;
    --lime: #8dc21f;
    --forest: #3d5421;
    --bar: #4e6d1f;
    --text: #ffffff;
  }
  html, body {
    margin: 0;
    padding: 0;
    width: 1200px;
    height: 1000px;
    overflow: hidden;
    background: var(--page);
  }
  .menu-board {
    position: absolute;
    left: 0;
    top: 163px;
    width: 1200px;
    height: 674px;
    background: var(--board);
    overflow: hidden;
    font-family: "Questrial", sans-serif;
    color: var(--text);
  }
  .board-art {
    position: absolute;
    inset: 0;
    width: 1200px;
    height: 674px;
  }
  .brand {
    position: absolute;
    left: 221px;
    top: 50px;
    width: 194px;
    display: flex;
    align-items: center;
    justify-content: flex-end;
    gap: 8px;
    font-size: 31px;
    letter-spacing: 1px;
    line-height: 1;
    color: var(--lime);
  }
  .brand-dot {
    width: 12px;
    height: 12px;
    border-radius: 50%;
    background: var(--lime);
  }
  .section-title {
    position: absolute;
    margin: 0;
    font-family: "Oswald", sans-serif;
    font-weight: 700;
    font-size: 31px;
    letter-spacing: 9px;
    line-height: 1;
    color: var(--text);
  }
  .section-title.breakfast { right: 774px; top: 150px; margin-right: -9px; }
  .section-title.lunch { left: 536px; top: 54px; }
  .menu-list {
    position: absolute;
    margin: 0;
    padding: 0;
    list-style: none;
    font-size: 18px;
    letter-spacing: 0.4px;
    line-height: 1.2;
  }
  .menu-list li {
    position: absolute;
    left: 0;
    display: flex;
    justify-content: space-between;
    white-space: nowrap;
  }
  .breakfast-list { left: 62px; top: 0; }
  .breakfast-list li { width: 353px; }
  .lunch-list { left: 536px; top: 0; }
  .lunch-list li { width: 382px; }
  .lunch-list .price { width: 50px; text-align: left; }
</style>
</head>
<body>
<main class="menu-board">
  <svg class="board-art" viewBox="0 0 1200 674" xmlns="http://www.w3.org/2000/svg">
    <defs>
      <linearGradient id="omelette-tone" x1="0" y1="0" x2="1" y2="1">
        <stop offset="0" stop-color="#e2ddd6"/>
        <stop offset="1" stop-color="#d9b25a"/>
      </linearGradient>
      <linearGradient id="pancake-tone" x1="0" y1="0" x2="0" y2="1">
        <stop offset="0" stop-color="#e4e6e8"/>
        <stop offset="1" stop-color="#cdb69a"/>
      </linearGradient>
      <linearGradient id="wrap-tone" x1="0" y1="0" x2="1" y2="1">
        <stop offset="0" stop-color="#e2e3e5"/>
        <stop offset="1" stop-color="#b9977a"/>
      </linearGradient>
      <linearGradient id="pasta-tone" x1="0" y1="0" x2="0" y2="1">
        <stop offset="0" stop-color="#ececec"/>
        <stop offset="1" stop-color="#c95a36"/>
      </linearGradient>
    </defs>

    <rect class="decor-area" x="0" y="0" width="192" height="148" fill="var(--lime)"
          role="img" aria-label="Decorative lime leaf"/>
    <rect class="decor-area" x="710" y="0" width="488" height="96" fill="var(--forest)"
          role="img" aria-label="Decorative row of dark green leaves"/>
    <rect class="decor-area" x="280" y="582" width="220" height="92" fill="var(--forest)"
          role="img" aria-label="Decorative dark green leaf"/>
    <rect class="decor-area" x="1058" y="534" width="142" height="140" fill="var(--forest)"
          role="img" aria-label="Decorative dark green leaf"/>

    <rect class="divider" x="465" y="0" width="13" height="319" fill="var(--bar)"/>

    <circle cx="80" cy="554" r="186" fill="url(#omelette-tone)" stroke="var(--lime)" stroke-width="13"
            role="img" aria-label="Photo of an omelette with toast"/>
    <circle cx="403" cy="458" r="110" fill="url(#pancake-tone)" stroke="var(--lime)" stroke-width="13"
            role="img" aria-label="Photo of chocolate chip pancakes"/>
    <circle cx="1134" cy="335" r="165" fill="url(#wrap-tone)" stroke="var(--lime)" stroke-width="13"
            role="img" aria-label="Photo of a steak wrap cut in half"/>
    <rect x="529" y="470" width="522" height="204" fill="url(#pasta-tone)"
          role="img" aria-label="Photo of meatball fettuccine in a white bowl"/>
  </svg>

  <div class="brand"><span class="brand-dot"></span><span>GREENLEAF</span></div>

  <h2 class="section-title breakfast">BREAKFAST</h2>
  <ul class="menu-list breakfast-list">
    <li style="top:207px"><span>Protein Chocolate Chip Pancakes</span><span class="price">$12.95</span></li>
    <li style="top:250px"><span>Sunny Trail Burrito</span><span class="price">$11.95</span></li>
    <li style="top:292px"><span>Tall Barn Omelette</span><span class="price">$12.95</span></li>
  </ul>

  <h2 class="section-title lunch">LUNCH</h2>
  <ul class="menu-list lunch-list">
    <li style="top:107px"><span>Butter Chicken</span><span class="price">$13.95</span></li>
    <li style="top:138px"><span>Chicken Quesadilla</span><span class="price">$13.45</span></li>
    <li style="top:169px"><span>Coconut Garlic Shrimp</span><span class="price">$15.95</span></li>
    <li style="top:200px"><span>Goat Cheese Stuffed Chicken</span><span class="price">$14.95</span></li>
    <li style="top:232px"><span>Chipotle Steak Wrap</span><span class="price">$12.95</span></li>
    <li style="top:263px"><span>Turkey Meatball Fettuccini</span><span class="price">$13.45</span></li>
    <li style="top:294px"><span>Chicken Alfredo</span><span class="price">$13.45</span></li>
    <li style="top:325px"><span>Chicken Parmesan</span><span class="price">$13.95</span></li>
    <li style="top:357px"><span>Pesto Chicken Pasta</span><span class="price">$13.45</span></li>
    <li style="top:388px"><span>Steak Bite and Green Stir Fry</span><span class="price">$13.45</span></li>
    <li style="top:419px"><span>Asian Chicken Teriyaki</span><span class="price">$13.45</span></li>
  </ul>
</main>
</body>
</html>
```